Structural Engineering Business Card

Veltrow Drafts does residential house plans for clients in Central Florida. Would like simple but elegant business card that is appropriate for a house plan engineering company. Prefer black business card with black/white them but open to other shades of blue. I uploaded a sample card that I came across that looked good but please come up with your own creative designs.

Contact Information for Business Card

Name, Title, Phone, Email, Address, website

```html
<!DOCTYPE html>
<html lang="en">
<head>
<meta charset="utf-8">
<title>Veltrow Drafts — Business Card</title>
<link rel="stylesheet" href="https://fonts.googleapis.com/css2?family=Sora:wght@300;400;700;800&display=swap">
<style>
  :root {
    --backdrop: #cbcbcb;
    --card-light: #ffffff;
    --card-dark: #000000;
    --ink: #000000;
    --ink-soft: #555555;
    --paper-text: #ffffff;
  }
  * { margin: 0; padding: 0; box-sizing: border-box; }
  html, body {
    width: 1200px;
    height: 1200px;
    overflow: hidden;
    background: var(--backdrop);
    font-family: "Sora", sans-serif;
  }
  .sheet {
    position: relative;
    width: 1200px;
    height: 1200px;
  }
  .card {
    position: absolute;
    left: 180px;
    width: 840px;
    height: 480px;
  }
  .card--front {
    top: 100px;
    background: var(--card-light);
    color: var(--ink);
  }
  .card--back {
    top: 620px;
    background: var(--card-dark);
    color: var(--paper-text);
    display: flex;
    align-items: center;
    justify-content: center;
  }
  .holder {
    position: absolute;
    left: 64px;
    top: 66px;
  }
  .holder__name {
    font-weight: 800;
    font-size: 30px;
    letter-spacing: 0.5px;
    text-transform: uppercase;
  }
  .holder__title {
    font-weight: 300;
    font-size: 22px;
    color: var(--ink-soft);
    margin-top: 2px;
  }
  .contacts {
    position: absolute;
    left: 64px;
    top: 300px;
    list-style: none;
    font-weight: 300;
    font-size: 21px;
    color: var(--ink-soft);
  }
  .contacts__item {
    display: flex;
    align-items: flex-start;
    gap: 14px;
    line-height: 28px;
    margin-bottom: 4px;
  }
  .contacts__icon {
    flex: none;
    width: 24px;
    height: 24px;
    margin-top: 2px;
  }
  .wordmark {
    display: flex;
    align-items: center;
    gap: 14px;
    font-weight: 800;
    text-transform: uppercase;
    letter-spacing: 1px;
  }
  .wordmark__square {
    background: currentColor;
  }
  .card--front .wordmark {
    position: absolute;
    right: 60px;
    top: 200px;
    font-size: 34px;
  }
  .card--front .wordmark__square { width: 22px; height: 22px; }
  .card--back .wordmark { font-size: 58px; }
  .card--back .wordmark__square { width: 36px; height: 36px; }
</style>
</head>
<body>
<main class="sheet">

  <section class="card card--front" aria-label="Business card front">
    <header class="holder">
      <h1 class="holder__name">Dorian Keswick</h1>
      <p class="holder__title">Owner</p>
    </header>

    <ul class="contacts">
      <li class="contacts__item">
        <svg class="contacts__icon" viewBox="0 0 24 24" aria-hidden="true">
          <circle cx="12" cy="12" r="12" fill="#000"/>
          <path d="M8.5 6.5l2 2.3-1.2 1.4c.8 1.7 2 2.9 3.6 3.7l1.4-1.2 2.3 2-1.1 1.8c-4.2-.4-8-4.2-8.5-8.6z" fill="#fff"/>
        </svg>
        <span>(555) 010-4827</span>
      </li>
      <li class="contacts__item">
        <svg class="contacts__icon" viewBox="0 0 24 24" aria-hidden="true">
          <circle cx="12" cy="12" r="12" fill="#000"/>
          <rect x="6" y="8" width="12" height="8.5" fill="none" stroke="#fff" stroke-width="1.6"/>
          <path d="M6 8l6 5 6-5" fill="none" stroke="#fff" stroke-width="1.6"/>
        </svg>
        <span>hello@veltrowdrafts.com</span>
      </li>
      <li class="contacts__item">
        <svg class="contacts__icon" viewBox="0 0 24 24" aria-hidden="true">
          <circle cx="12" cy="12" r="12" fill="#000"/>
          <g fill="none" stroke="#fff" stroke-width="1.4">
            <circle cx="12" cy="12" r="6"/>
            <ellipse cx="12" cy="12" rx="2.6" ry="6"/>
            <path d="M6 12h12"/>
          </g>
        </svg>
        <span>www.veltrowdrafts.com</span>
      </li>
      <li class="contacts__item">
        <svg class="contacts__icon" viewBox="0 0 24 24" aria-hidden="true">
          <circle cx="12" cy="12" r="12" fill="#000"/>
          <path d="M12 5.5a4.5 4.5 0 0 0-4.5 4.5c0 3.3 4.5 8.5 4.5 8.5s4.5-5.2 4.5-8.5A4.5 4.5 0 0 0 12 5.5z" fill="#fff"/>
          <circle cx="12" cy="10" r="1.7" fill="#000"/>
        </svg>
        <span>218 Orchard Bend Lane,<br>Orlando, FL 32801</span>
      </li>
    </ul>

    <div class="wordmark">
      <span class="wordmark__square" aria-hidden="true"></span>
      <span class="wordmark__name">Veltrow Drafts</span>
    </div>
  </section>

  <section class="card card--back" aria-label="Business card back">
    <div class="wordmark">
      <span class="wordmark__square" aria-hidden="true"></span>
      <span class="wordmark__name">Veltrow Drafts</span>
    </div>
  </section>

</main>
</body>
</html>
```